Brisk Lending Benefits Summary

We are looking to put our benefits information into a summary document and make it look pretty/easy to read! I put all of the information together into a document, one tab for all of our medical plans and another for dental/vision. This document is only there as a guide. I want this to be visually appealing, so feel free to get creative with the format.

Industry/Entity Type

Mortgage Lender

Colors
31b7a3
ffcf3e

Requirements
Should not have
• I don't want a copy and pasted version of the visual I sent, with our logo attached.

```html
<!DOCTYPE html>
<html lang="en">
<head>
<meta charset="utf-8">
<title>Brisk Lending Benefits Summary</title>
<link href="https://fonts.googleapis.com/css2?family=Montserrat:wght@400;700;800&family=Open+Sans:wght@400;600;700&display=swap" rel="stylesheet">
<style>
:root{
  --bg:#e9e6d2;
  --paper:#ffffff;
  --yellow:#f7e200;
  --teal:#3bb7d2;
  --teal-dark:#2fa8c4;
  --teal-light:#4bc1d9;
  --teal-brand:#2bb3d3;
  --head-grey:#e1e4e6;
  --ink:#1c3544;
  --ink-soft:#2b4656;
  --line:rgba(255,255,255,.35);
}
*{box-sizing:border-box;margin:0;padding:0}
html,body{width:1200px;height:2400px;overflow:hidden;background:var(--bg)}
body{font-family:"Open Sans",Arial,sans-serif;color:var(--ink);position:relative}
.page{position:absolute;left:0;width:1200px;height:850px;background:var(--paper);overflow:hidden;box-shadow:0 6px 18px rgba(0,0,0,.12)}
.page--medical{top:90px}
.page--extras{top:1040px}
.page-header{position:absolute;left:0;top:0;width:1200px;height:100px}
.brand{position:absolute;left:40px;top:44px;font-family:"Montserrat",sans-serif;font-weight:800;color:var(--teal-brand);font-size:30px;line-height:32px;letter-spacing:-.5px}
.doc-title{position:absolute;left:428px;top:28px;white-space:nowrap;display:flex;align-items:baseline;gap:18px}
.doc-title__main{font-family:"Montserrat",sans-serif;font-weight:800;font-size:25px;color:var(--teal-brand);letter-spacing:-.3px}
.doc-title__word{font-family:"Montserrat",sans-serif;font-weight:400;font-size:25px;color:var(--ink);letter-spacing:17px}
.page-footer{position:absolute;left:0;top:738px;width:1200px;height:112px;background:var(--yellow);border-top:6px solid var(--teal-brand)}
.page-footer p{position:absolute;left:53px;right:40px;font-size:8.6px;line-height:15px;color:var(--ink-soft)}
.page--medical .page-footer p{top:40px}
.page--extras .page-footer p{top:26px}

table{border-collapse:collapse;position:absolute;z-index:2;table-layout:fixed}
td,th{font-size:8.6px;line-height:1.3;vertical-align:middle}
th{background:var(--head-grey);font-weight:700;color:var(--ink);font-size:8.4px;text-align:center;border:1px solid #fff}

.medical-table{left:53px;top:135px;width:1092px}
.medical-table td{text-align:center;background:var(--teal);border-bottom:1px solid var(--line);padding:0 2px}
.medical-table td.non{background:var(--teal-dark)}
.medical-table td.label{background:var(--teal-light);text-align:left;padding-left:12px}
.medical-table .plan-row th{height:31px;font-size:7.6px;letter-spacing:-.1px}
.medical-table .net-row th{height:31px}
.medical-table .cost-row td{background:var(--teal);border-bottom:none}
.sub{display:block;padding-left:10px}
.sub2{display:block;padding-left:16px}
.tag{display:block;color:#fff;font-weight:700}
.gap{display:block;height:8px}

.section-title{position:absolute;font-family:"Montserrat",sans-serif;font-weight:800;font-size:15px;color:var(--teal-brand);text-align:center;letter-spacing:.3px}
.section-title--vision{left:57px;width:522px;top:130px;text-align:left;padding-left:238px}
.section-title--dental{left:615px;width:539px;top:198px}

.vision-table{left:57px;top:155px;width:522px}
.vision-table td{background:var(--teal);text-align:center;border-bottom:1px solid var(--line);border-left:1px solid var(--line);padding:0 4px}
.vision-table td.label{text-align:left;padding-left:20px;border-left:none}
.vision-table td.label.center{text-align:center;padding-left:0}
.vision-table th{height:24px}

.dental-table{left:615px;top:226px;width:539px}
.dental-table td{background:var(--teal);text-align:center;border-bottom:1px solid var(--line);border-left:1px solid var(--line);padding:0 6px}
.dental-table td.label{text-align:left;padding-left:20px;border-left:none}
.dental-table td.note{text-align:left;padding:0 14px 0 20px}
.dental-table th{height:21px}
.dental-table .band th{background:var(--teal);color:var(--ink);border:none;border-bottom:1px solid var(--line);height:25px}
.dental-table .band th.sub-head{background:var(--teal);font-weight:700}
.grey-block{display:block;height:18px;background:#707478;margin:4px -6px -4px}
</style>
</head>
<body>

<section class="page page--medical">
  <svg class="page-header" viewBox="0 0 1200 100" aria-hidden="true">
    <rect x="0" y="0" width="1200" height="7" fill="var(--yellow)"/>
    <rect x="0" y="14" width="258" height="6" fill="var(--teal-brand)"/>
    <polygon points="380,0 1200,0 1200,88 436,88" fill="var(--yellow)"/>
    <polygon points="436,88 1200,88 1200,95 441,95" fill="var(--teal-brand)"/>
    <polygon points="258,14 284,14 334,88 308,88" fill="var(--teal-brand)"/>
    <polygon points="296,14 322,14 372,88 346,88" fill="var(--teal-brand)"/>
    <polygon points="334,14 360,14 410,88 384,88" fill="var(--teal-brand)"/>
  </svg>
  <div class="brand">Brisk<br>Lending</div>
  <h1 class="doc-title"><span class="doc-title__main">BRISK LENDING BENEFITS</span><span class="doc-title__word">SUMMARY</span></h1>

  <table class="medical-table">
    <colgroup>
      <col style="width:167px"><col style="width:92px"><col style="width:93px"><col style="width:92px"><col style="width:93px"><col style="width:92px"><col style="width:93px"><col style="width:92px"><col style="width:93px"><col style="width:92px"><col style="width:93px">
    </colgroup>
    <tr class="plan-row">
      <th style="background:#fff;border:none"></th>
      <th colspan="2">Crestline Gold PPO 2250/0%/2250 w/HSA TradRX</th>
      <th colspan="2">Crestline Silver PPO 3500/50%/7900 TradRX</th>
      <th colspan="2">Crestline Gold Pathway HMO 1000/20%/5600</th>
      <th colspan="2">Crestline Gold PPO 750/20%/5250</th>
      <th colspan="2">Crestline Platinum PPO 250/20%/3500</th>
    </tr>
    <tr class="net-row">
      <th style="background:#fff;border:none"></th>
      <th>In-Network</th><th>Non-Network</th><th>In-Network</th><th>Non-Network</th><th>In-Network</th><th>Non-Network</th><th>In-Network</th><th>Non-Network</th><th>In-Network</th><th>Non-Network</th>
    </tr>
    <tr style="height:50px">
      <td class="label">Annual Deductible<span class="sub">Single / Family</span></td>
      <td>$2,250 / $4,500</td><td class="non">$6,750 / $13,500</td>
      <td>$3,500 / $7,000</td><td class="non">$10,500 / $21,000</td>
      <td>$1,000 / $3,000</td><td class="non">Not covered</td>
      <td>$750 / $2,250</td><td class="non">$2,250 / $4,500</td>
      <td>$250 / $750</td><td class="non">$2,000 / $4,000</td>
    </tr>
    <tr style="height:44px">
      <td class="label">Annual Out-of-Pocket Maximum<span class="sub">Single / Family</span></td>
      <td>$2,250 / $4,500</td><td class="non">$7,875 / $15,750</td>
      <td>$7,900 / $15,800</td><td class="non">$23,700 / $47,400</td>
      <td>$5,600 / $11,200</td><td class="non">Not covered</td>
      <td>$5,250 / $10,500</td><td class="non">$15,750 / $31,500</td>
      <td>$3,500 / $7,000</td><td class="non">$10,500 / $21,000</td>
    </tr>
    <tr style="height:42px">
      <td class="label">Office Visit<span class="sub">Primary Care</span><span class="sub">Specialist</span></td>
      <td>0% coinsurance<br>0% coinsurance</td><td class="non">50% coinsurance<br>50% coinsurance</td>
      <td>$50/visit<br>$75/visit</td><td class="non">50% coinsurance<br>50% coinsurance</td>
      <td>$25/visit<br>$50/visit</td><td class="non">Not covered<br>Not covered</td>
      <td style="font-size:7.4px;line-height:1.15">$20/visit for first 3, then 20% coinsurance<br>$20/visit for first 3, then 20% coinsurance</td><td class="non">50% coinsurance<br>50% coinsurance</td>
      <td>$15/visit<br>$25/visit</td><td class="non">50% coinsurance<br>50% coinsurance</td>
    </tr>
    <tr style="height:24px">
      <td class="label">Preventative Services</td>
      <td>No charge</td><td class="non">50% coinsurance</td>
      <td>No charge</td><td class="non">50% coinsurance</td>
      <td>No charge</td><td class="non">Not covered</td>
      <td>No charge</td><td class="non">50% coinsurance</td>
      <td>No charge</td><td class="non">50% coinsurance</td>
    </tr>
    <tr style="height:25px">
      <td class="label">Diagnostic Test &amp; Imaging</td>
      <td>0% coinsurance</td><td class="non">50% coinsurance</td>
      <td>50% coinsurance</td><td class="non">50% coinsurance</td>
      <td>20% coinsurance</td><td class="non">Not covered</td>
      <td>20% coinsurance</td><td class="non">50% coinsurance</td>
      <td>20% coinsurance</td><td class="non">50% coinsurance</td>
    </tr>
    <tr style="height:25px">
      <td class="label">Outpatient Surgery</td>
      <td>0% coinsurance</td><td class="non">50% coinsurance</td>
      <td>50% coinsurance</td><td class="non">50% coinsurance</td>
      <td>20% coinsurance</td><td class="non">Not covered</td>
      <td>20% coinsurance</td><td class="non">50% coinsurance</td>
      <td>20% coinsurance</td><td class="non">50% coinsurance</td>
    </tr>
    <tr style="height:66px">
      <td class="label">Emergency<span class="sub">Emergency Room</span><span class="sub">Emergency Medical Transportation</span><span class="sub">Urgent Care</span></td>
      <td><br>0% coinsurance<br>0% coinsurance<br>0% coinsurance</td><td class="non"><br>Covered as In-Network<br>Covered as In-Network<br>50% coinsurance</td>
      <td><br>$500/visit<br>50% coinsurance<br>$75/visit</td><td class="non"><br>Covered as In-Network<br>Covered as In-Network<br>50% coinsurance</td>
      <td><br>$300/visit<br>20% coinsurance<br>$50/visit</td><td class="non"><br>Not covered<br>Not covered<br>Not covered</td>
      <td><br>$300/visit<br>$300/trip<br>20% coinsurance</td><td class="non"><br>Covered as In-Network<br>Covered as In-Network<br>50% coinsurance</td>
      <td><br>$300/visit<br>20% coinsurance<br>$25/visit</td><td class="non"><br>Covered as In-Network<br>Covered as In-Network<br>50% coinsurance</td>
    </tr>
    <tr style="height:23px">
      <td class="label">Hospital Stay</td>
      <td>0% coinsurance</td><td class="non">50% coinsurance</td>
      <td>50% coinsurance</td><td class="non">50% coinsurance</td>
      <td>20% coinsurance</td><td class="non">Not covered</td>
      <td>20% coinsurance</td><td class="non">50% coinsurance</td>
      <td>20% coinsurance</td><td class="non">50% coinsurance</td>
    </tr>
    <tr style="height:80px">
      <td class="label">Mental Health/Behavioral<br>Health/Substance Abuse Services<span class="gap"></span><span class="sub">Outpatient Services</span><span class="gap"></span><span class="sub">Inpatient Services</span></td>
      <td><span class="tag">Office Visit</span>0% coinsurance<span class="tag">Other Outpatient</span>0% coinsurance<span class="gap"></span>0% coinsurance</td>
      <td class="non"><span class="tag">Office Visit</span>50% coinsurance<span class="tag">Other Outpatient</span>50% coinsurance<span class="gap"></span>50% coinsurance</td>
      <td><span class="tag">Office Visit</span>$50/visit<span class="tag">Other Outpatient</span>50% coinsurance<span class="gap"></span>50% coinsurance</td>
      <td class="non"><span class="tag">Office Visit</span>50% coinsurance<span class="tag">Other Outpatient</span>50% coinsurance<span class="gap"></span>50% coinsurance</td>
      <td><span class="tag">Office Visit</span>$25/visit<span class="tag">Other Outpatient</span>20% coinsurance<span class="gap"></span>20% coinsurance</td>
      <td class="non">Not covered<br>Not covered</td>
      <td style="line-height:1.15"><span class="tag">Office Visit</span>$20/visit for first 3, then 20% coinsurance<span class="tag">Other Outpatient</span>20% coinsurance<br>20% coinsurance</td>
      <td class="non"><span class="tag">Office Visit</span>50% coinsurance<span class="tag">Other Outpatient</span>50% coinsurance<br>50% coinsurance</td>
      <td><span class="tag">Office Visit</span>$15/visit<span class="tag">Other Outpatient</span>20% coinsurance<br>20% coinsurance</td>
      <td class="non"><span class="tag">Office Visit</span>50% coinsurance<span class="tag">Other Outpatient</span>50% coinsurance<br>50% coinsurance</td>
    </tr>
    <tr style="height:57px">
      <td class="label">Pregnancy<span class="sub">Office visits, childbirth/delivery</span><span class="sub">professional &amp; facility services</span></td>
      <td>0% coinsurance</td><td class="non">50% coinsurance</td>
      <td>50% coinsurance</td><td class="non">50% coinsurance</td>
      <td>20% coinsurance</td><td class="non">Not covered</td>
      <td>20% coinsurance</td><td class="non">50% coinsurance</td>
      <td>20% coinsurance</td><td class="non">50% coinsurance</td>
    </tr>
    <tr class="cost-row" style="height:140px">
      <td class="label">Monthly Cost (Varies by Age)*<br>Age 30<span class="sub">Employee</span><span class="sub">Per Child Cost**</span><span class="sub">Spouse/Domestic Partner Cost</span>Age 50<span class="sub">Employee</span><span class="sub">Per Child Cost**</span><span class="sub">Spouse/Domestic Partner Cost</span></td>
      <td colspan="2"><br><br>$134<br>$181<br>$268<br><br>$211<br>$181<br>$422</td>
      <td colspan="2"><br><br>$111<br>$150<br>$222<br><br>$175<br>$150<br>$350</td>
      <td colspan="2"><br><br>$114<br>$155<br>$229<br><br>$180<br>$155<br>$361</td>
      <td colspan="2"><br><br>$136<br>$184<br>$273<br><br>$215<br>$184<br>$431</td>
      <td colspan="2"><br><br>$149<br>$201<br>$299<br><br>$235<br>$201<br>$471</td>
    </tr>
  </table>

  <footer class="page-footer">
    <p>Limitations, exceptions and other important information are provided in the summary of benefits and coverage for each plan. In the event that the information in this summary differs from the plan description, the plan description will prevail.<br>
    *For the purpose of this document, we assume that your spouse is the same age as you and that your children are 18 years old or less. Your quoted price will change based on the actual age of your spouse and children.<br>
    **Children beyond the first three are covered at no additional cost.</p>
  </footer>
</section>

<section class="page page--extras">
  <svg class="page-header" viewBox="0 0 1200 100" aria-hidden="true">
    <rect x="0" y="0" width="1200" height="7" fill="var(--yellow)"/>
    <rect x="0" y="14" width="258" height="6" fill="var(--teal-brand)"/>
    <polygon points="380,0 1200,0 1200,88 436,88" fill="var(--yellow)"/>
    <polygon points="436,88 1200,88 1200,95 441,95" fill="var(--teal-brand)"/>
    <polygon points="258,14 284,14 334,88 308,88" fill="var(--teal-brand)"/>
    <polygon points="296,14 322,14 372,88 346,88" fill="var(--teal-brand)"/>
    <polygon points="334,14 360,14 410,88 384,88" fill="var(--teal-brand)"/>
  </svg>
  <div class="brand">Brisk<br>Lending</div>
  <h1 class="doc-title"><span class="doc-title__main">BRISK LENDING BENEFITS</span><span class="doc-title__word">SUMMARY</span></h1>

  <h2 class="section-title section-title--vision">VISION</h2>
  <table class="vision-table">
    <colgroup><col style="width:188px"><col style="width:167px"><col style="width:167px"></colgroup>
    <tr><th></th><th>In-Network</th><th>Non-Network</th></tr>
    <tr style="height:88px">
      <td class="label">Co-Pay<span class="sub">First Service Provided</span><span class="sub">Exams</span><br><span class="sub">Materials</span></td>
      <td colspan="2">Not applicable<br>Exams $10.00<br>$25<br>Waived for conventional &amp; planned replacement contact lenses</td>
    </tr>
    <tr style="height:88px">
      <td class="label">How Often Can I Obtain Service?*<span class="sub">Exams</span><span class="sub">Lenses</span><span class="sub">Frames</span><span class="sub">Materials</span></td>
      <td colspan="2"><br>Once/year<br>Once/year<br>Once every other year<br>Once/year</td>
    </tr>
    <tr style="height:25px">
      <td class="label center">Eye Exams</td><td>Copay applies</td><td>Amount over $39</td>
    </tr>
    <tr style="height:75px">
      <td class="label">Lenses<span class="sub">Single Vision</span><span class="sub">Lined Bifocal</span><span class="sub">Lined Trifocal</span><span class="sub">Lenticular</span></td>
      <td><br>Copay applies<br>Copay applies<br>Copay applies<br>Copay applies</td>
      <td><br>Amount over $23<br>Amount over $37<br>Amount over $49<br>Amount over $64</td>
    </tr>
    <tr style="height:94px">
      <td class="label">Contact Lenses<span class="sub">Conventional</span><span class="sub">Planned Replacement &amp; Disposable</span><span class="sub">Medically Necessary</span><span class="sub">Evaluation &amp; Fitting</span></td>
      <td><br>Amount over $130<br>Amount over $130<br>Copay applies<br>15% off professional fee</td>
      <td><br>Amount over $100<br>Amount over $100<br>Amount over $210<br>Not covered</td>
    </tr>
    <tr style="height:31px">
      <td class="label">Frames</td><td>$130, 20% discount on amount over $130</td><td>Amount over $46</td>
    </tr>
    <tr style="height:25px">
      <td class="label">Lens &amp; Frame Allowance</td><td>No discounts</td><td>No discounts</td>
    </tr>
    <tr style="height:31px">
      <td class="label">Cosmetic Extras</td><td>Discounted at average 20%-25% off providers UCR</td><td>No discounts</td>
    </tr>
    <tr style="height:38px">
      <td class="label">Laser Correction Surgery</td><td>Average 15% discount off usual price or 5% off promotional price</td><td>No discounts</td>
    </tr>
    <tr style="height:63px">
      <td class="label">Monthly Cost**<span class="sub">Employee</span><span class="sub">Child Cost***</span><span class="sub">Spouse/Domestic Partner Cost</span></td>
      <td colspan="2">$9<br>$7<br>$6</td>
    </tr>
  </table>

  <h2 class="section-title section-title--dental">DENTAL</h2>
  <table class="dental-table">
    <colgroup><col style="width:191px"><col style="width:87px"><col style="width:87px"><col style="width:87px"><col style="width:87px"></colgroup>
    <tr><th></th><th colspan="2">Calendar Year Deductible</th><th colspan="2">Coinsurance (Policy Pays)</th></tr>
    <tr><th></th><th>In-Network</th><th>Non-Network</th><th>In-Network</th><th>Non-Network</th></tr>
    <tr style="height:23px"><td class="label">Preventative</td><td>$0</td><td>$0</td><td>100%</td><td>100%</td></tr>
    <tr style="height:23px"><td class="label">Basic</td><td>$50</td><td>$50</td><td>80%</td><td>80%</td></tr>
    <tr style="height:24px"><td class="label">Major</td><td>$50</td><td>$50</td><td>50%</td><td>50%</td></tr>
    <tr style="height:65px"><td class="label">Combined Family Deductible</td><td class="note" colspan="4">Max deductible 3 times the per person deductible amount. Deductibles for basic and major procedures are combined for in-network and non-network.</td></tr>
    <tr style="height:42px"><td class="label">Combined Maximum</td><td class="note" colspan="4">Maximums for preventative, basic, and major procedures combined. In-network and non-network maximums are $1,000 per person.</td></tr>
    <tr class="band"><th colspan="5">Orthodontia - Child</th></tr>
    <tr class="band"><th></th><th class="sub-head">In-Network</th><th class="sub-head">Non-Network</th><th class="sub-head">In-Network</th><th class="sub-head">Non-Network</th></tr>
    <tr style="height:46px">
      <td class="label">Lifetime Deductible<br>Lifetime Maximum</td>
      <td>$0<br>$1,000</td><td>$0<br>$1,000</td>
      <td>50%<span class="grey-block"></span></td><td>50%<span class="grey-block"></span></td>
    </tr>
    <tr style="height:86px">
      <td class="label">Monthly Cost**<span class="sub">Employee</span><span class="sub">Child Cost***</span><span class="sub">Spouse/Domestic Partner Cost</span></td>
      <td colspan="4">$40<br>$68<br>$41</td>
    </tr>
  </table>

  <footer class="page-footer">
    <p>Limitations, exceptions and other important information are provided in the summary of benefits and coverage for each plan. In the event that the information in this summary differs from the plan description, the plan description will prevail.<br>
    **For the purpose of this document, we assume that your spouse is the same age as you and that your children are 18 years old or less. Your quoted price may change based on the actual age of your spouse and children.<br>
    ***Children beyond the first child are covered at no additional cost.<br>
    *Members will receive 20% off unlimited additional pairs of prescription glasses and non prescription sunglasses valid<br>
    through any ClearView doctor within 12 months of the last covered exam.</p>
  </footer>
</section>

</body>
</html>
```